Concert Venue Show Posters (ongoing job too)

Looking for a designer for ongoing project to create posters for each of our concerts coming to the venue. We have a budget of $35-45.00 per poster and on average do 5-12 per month. We’re looking for simple, unique design template going forward as part of our branding.

We hope to establish a long term relationship with someone to do this work on an ongoing adhoc basis.

Goal is to simple tell folks who, where, and when.

Creative needs to delivered in Photoshop PSD file format in two sizes; 24" x 36" used onsite in lobby and 11" x 17" for offsite marketing distribution.

We’ll supply all approved artwork and information for you to use although sometimes what we get from management sucks.

You can look at some of our older posters here
http://bramblehallvenue.example-photos.com/Other/Posters/

Our website (it’s in re-design now)
http://www.bramblehallvenue.example

Our new website format moving toward this as template
http://www.copperlanternhall.example/event/252331-kestrel-owls-portland/

Thoughts? Ideas? Included artwork to see some samples.

Include these items on poster
Bramble HALL logo
Artists Name
Dorian Pike and the Lanterns (image with single guitar players)
Velvet Anchor (group image)
September 25, 2014
Doors 7:00
Show 8:00
You can sort of get an idea from our old posters.

PS this could lead to extra work doing our newspaper creatives too.
Updates

Project Deadline Extended
Reason: Due to weekend and workload of staff we'll make our final selection on Wednesday, August 28th by 6 PM EST. Thanks to everyone for submitting some great examples of work.

Target Market(s)

Onsite concert goers for future shows, and offsite spreading the word about shows.

Industry/Entity Type

Marketing

Requirements
Must have
• Simple is best. Not looking for bar band type posters, remember we're just letting fans know about who and when.
Nice to have
• Template, easy to reproduce show after show to keep costs down.
Should not have
• Less is more since we're just telling patons who, when, and where.

```html
<!DOCTYPE html>
<html lang="en">
<head>
<meta charset="utf-8">
<title>Bramble HALL presents Dorian Pike and the Lanterns</title>
<link href="https://fonts.googleapis.com/css2?family=Oswald:wght@500;700&display=swap" rel="stylesheet">
<style>
  :root {
    --page-bg: #ffffff;
    --band-gold: #e2c126;
    --band-gold-deep: #c9a323;
    --stage-yellow: #d8c23a;
    --stage-amber: #b08a2a;
    --stage-magenta: #9a4a7a;
    --night-olive: #3a3c1c;
    --night-black: #0b0b08;
    --ink-white: #f4f4f0;
  }
  * { margin: 0; padding: 0; box-sizing: border-box; }
  html, body {
    width: 1200px; height: 1000px; overflow: hidden;
    background: var(--page-bg);
    font-family: "Oswald", "Arial Narrow", sans-serif;
  }
  .poster {
    position: absolute; left: 312px; top: 18px;
    width: 626px; height: 970px; overflow: hidden;
    background: linear-gradient(180deg, var(--night-olive) 0%, #1c1d10 55%, var(--night-black) 100%);
    box-shadow: 3px 4px 6px rgba(0,0,0,0.45);
    color: var(--ink-white);
  }
  .venue-band {
    position: absolute; left: 0; top: 0; width: 626px; height: 144px;
    background: linear-gradient(90deg, var(--band-gold-deep) 0%, var(--band-gold) 60%, var(--band-gold) 100%);
  }
  .venue-name {
    position: absolute; left: 190px; top: 18px;
    font-weight: 700; font-size: 52px; line-height: 1; letter-spacing: 1px;
    color: var(--ink-white);
  }
  .venue-present {
    position: absolute; left: 344px; top: 92px;
    font-weight: 700; font-size: 34px; line-height: 1; letter-spacing: 1px;
    color: var(--ink-white);
  }
  .artist-photo {
    position: absolute; left: 0; top: 144px; width: 626px; height: 486px;
    background:
      radial-gradient(ellipse at 48% 30%, rgba(154,74,122,0.55) 0%, rgba(154,74,122,0) 45%),
      radial-gradient(ellipse at 50% 55%, var(--stage-yellow) 0%, var(--stage-amber) 70%, #5a4a1a 100%);
  }
  .headliner {
    position: absolute; left: 0; width: 626px; text-align: center;
    font-weight: 700; text-transform: uppercase; line-height: 1;
  }
  .headliner-name { top: 560px; font-size: 78px; letter-spacing: 3px; }
  .headliner-tail { top: 648px; font-size: 46px; letter-spacing: 1px; }
  .headliner-tail .small { text-transform: none; }
  .show-time {
    position: absolute; left: 84px; width: 446px; text-align: center;
  }
  .rule-row { display: flex; align-items: center; gap: 14px; }
  .rule-row::before, .rule-row::after {
    content: ""; flex: 1; height: 2px; background: var(--ink-white);
  }
  .weekday { top: 752px; font-weight: 700; font-size: 30px; letter-spacing: 2px; line-height: 1; }
  .date { top: 792px; width: 446px; font-weight: 700; font-size: 46px; letter-spacing: 3px; line-height: 1; }
  .start { top: 855px; font-weight: 500; font-size: 20px; letter-spacing: 1px; line-height: 1; }
  .venue-address {
    position: absolute; left: 0; top: 932px; width: 626px; text-align: center;
    font-weight: 500; font-size: 17px; letter-spacing: 0.6px; line-height: 1;
  }
</style>
</head>
<body>
  <main class="poster">
    <header class="venue-band">
      <div class="venue-name">Bramble HALL</div>
      <div class="venue-present">PRESENT</div>
    </header>
    <div class="artist-photo" role="img" aria-label="Concert photo of the guitarist playing an electric guitar under yellow and pink stage lights"></div>
    <h1 class="headliner headliner-name">Dorian Pike</h1>
    <div class="headliner headliner-tail"><span class="small">and</span> THE LANTERNS</div>
    <div class="show-time rule-row weekday">THURSDAY</div>
    <div class="show-time date">SEPTEMBER 25, 2014</div>
    <div class="show-time rule-row start">SHOW AT 8:00 PM</div>
    <footer class="venue-address">180 W. LARKSPUR ST. MILLBROOK, FL 32990 WWW.BRAMBLEHALLVENUE.EXAMPLE</footer>
  </main>
</body>
</html>
```